Verdant Harbor wants proposals to design and develop a new website, tying together the visuals and branding message initiated with the package design. The goals of this website will be to provide an excellent user experience, to make the website a vital source of information that
will be indexed by the search engines and to facilitate and encourage consumer confidence.
The design and function of the website will be instrumental in generating knowledge of and trust in the product line.

Our current website Verdantharbor.com is an informational and transactional website. We are looking to completely overhaul the informational side. The products we sell are unique combinations of Ayurvedic herbal supplements. They are very effective and of a superior quality. However, the current website in all fairness is "blah". The site should be professional, visually enticing, reliable and efficient, compatible with virtually any computer that connects to it and makes for a first rate impression to our customers.

We want a website which will relay to the customer the effectiveness and superior quality of our products. We want the site to engage the customer. The website needs to be an experience and to connect to the customer emotionally. It is a tall order but it is what we need to deliver our message. A majority of the traffic comes from people already interested in a particular condition that our product is used for. Our goal is for the customer to be convinced that the solution is our product which it is in most cases.

The design should be able to handle fields that are currently on the site, like article links to external sites, video clips on products, specials, etc. The site is currently powered on the back end by .NET 4.0 with MVC architecture and this we hope to continue. Also, the text to HTML has to be a very good ratio.

The current pages are very well indexed and search engine optimized and that concept has to be preserved. At this point, we do not want to build a separate mobile version so flash is not an option.
Updates

Pleas come up with original ideas and not just refreshing currently what I have.

Pictures used need to be realistic.  Faces are ok to use but not necessary.  The picture/graphic needs to communicate effectiveness and high quality of products.  Also the overall look and feel needs to be addressed.  Please don't take existing part of current website and paste onto new one.  

We are disappointed in the overall designs received.  They all look like cut and paste websites. One that we did like was showing herbs held in the hand.  We are not opposed to faces being shown but it has to look "real".  Also the space below the picture needs to be developed more.  We are not focusing on transactions on this website although a link will be provided for those interested in purchasing.

After reviewing all designs, it seems showing herbs/flowers/nature is a better way to go.  The picture of women makes our company look more like a spa which is not our intent.  

Target Market(s)

USA, Canada, Western European customers; 60% Females, 40% male; 35 plus age group

Industry/Entity Type

Architecture

Requirements
Must have
• Good Text to Html ratio. Should be SEO compatible. Feel good and engaging audience.
Should not have
• Must be mobile compatible and should not be flash based.

```html
<!DOCTYPE html>
<html lang="en">
<head>
<meta charset="utf-8">
<title>Verdant Harbor – Featured Products</title>
<link rel="stylesheet" href="https://fonts.googleapis.com/css2?family=Ubuntu:ital,wght@0,300;0,400;0,500;0,700;1,400&display=swap">
<style>
  :root {
    --green-dark: #3f5f1c;
    --green-bright: #8cc43f;
    --green-line: #b9dc92;
    --card-border: #bfe09a;
    --text-body: #6a6a6a;
    --text-strong: #3a3a3a;
    --panel-bg: #fafafa;
    --page-bg: #ffffff;
    --caption-bg: rgba(40, 40, 40, 0.72);
  }
  * { box-sizing: border-box; margin: 0; padding: 0; }
  html, body { width: 1200px; height: 1073px; overflow: hidden; background: var(--page-bg); }
  body { font-family: "Ubuntu", sans-serif; color: var(--text-body); }

  .featured {
    height: 410px;
    background: var(--panel-bg);
    border-top: 2px solid var(--green-line);
    border-bottom: 2px solid var(--green-line);
    padding-top: 26px;
  }
  .section-title {
    text-align: center;
    font-size: 20px;
    font-weight: 700;
    letter-spacing: 0.3px;
    color: var(--green-dark);
  }
  .section-title span { color: var(--green-bright); }

  .product-grid {
    display: flex;
    justify-content: center;
    gap: 14px;
    margin-top: 36px;
  }
  .product-card {
    width: 178px;
    height: 270px;
    border: 2px solid var(--card-border);
    background: #fff;
    padding: 14px 12px 12px;
    text-align: center;
    display: flex;
    flex-direction: column;
  }
  .product-photo {
    height: 100px;
    margin: 0 12px;
    border-radius: 3px;
    background: linear-gradient(160deg, #e4e7a6 0%, #c8cf6c 55%, #b9a688 100%);
  }
  .product-name {
    margin-top: 12px;
    font-size: 11.5px;
    font-weight: 700;
    line-height: 16px;
    color: var(--green-dark);
    text-transform: uppercase;
  }
  .product-name span { display: block; color: var(--green-bright); font-weight: 500; }
  .product-rule {
    height: 2px;
    background: var(--green-line);
    margin: 6px 6px 10px;
  }
  .product-desc { font-size: 10.5px; line-height: 16px; font-weight: 300; }
  .product-link {
    margin-top: 6px;
    font-size: 9.5px;
    font-weight: 700;
    color: var(--green-dark);
  }
  .product-buy {
    margin-top: auto;
    display: flex;
    justify-content: space-between;
    align-items: center;
  }
  .price { font-size: 11px; font-weight: 700; color: var(--text-strong); }
  .buy-button {
    background: var(--green-bright);
    color: #fff;
    font-size: 9px;
    font-weight: 700;
    padding: 4px 9px;
    letter-spacing: 0.3px;
  }

  .tagline {
    margin: 38px auto 0;
    width: 580px;
    text-align: center;
    font-size: 11px;
    font-style: italic;
    line-height: 19px;
    color: var(--text-strong);
  }

  .standards {
    position: relative;
    display: flex;
    justify-content: center;
    gap: 64px;
    margin-top: 40px;
  }
  .decor {
    position: absolute;
    top: -10px;
    width: 90px;
    height: 230px;
    border-radius: 45px;
    background: linear-gradient(180deg, rgba(0,0,0,0.025), rgba(0,0,0,0.005));
  }
  .decor-left { left: 92px; }
  .decor-right { right: 92px; }

  .video {
    position: relative;
    width: 320px;
    height: 200px;
    background: radial-gradient(circle at 45% 40%, #4e8b2c 0%, #2f5e1c 55%, #5c4a32 100%);
  }
  .video-photo { position: absolute; inset: 0; }
  .video-play { position: absolute; left: 144px; top: 80px; }
  .video-caption {
    position: absolute;
    left: 0; right: 0; bottom: 0;
    height: 32px;
    background: var(--caption-bg);
    color: #fff;
    font-size: 11px;
    line-height: 32px;
    padding-left: 13px;
    text-transform: uppercase;
  }

  .standards-text { width: 370px; padding-top: 2px; }
  .standards-title {
    font-size: 14px;
    font-weight: 700;
    color: var(--green-dark);
    text-transform: uppercase;
  }
  .standards-list { list-style: none; margin-top: 20px; }
  .standards-list li {
    display: flex;
    gap: 8px;
    font-size: 10.5px;
    line-height: 15px;
    margin-bottom: 9px;
  }
  .standards-list svg { flex: none; margin-top: 2px; }
</style>
</head>
<body>
  <section class="featured">
    <h2 class="section-title">FEATURED <span>PRODUCTS</span></h2>
    <div class="product-grid">
      <article class="product-card">
        <div class="product-photo" role="img" aria-label="Product box of blood sugar supplement with capsules"></div>
        <h3 class="product-name">Blood Sugar<span>Supplements</span></h3>
        <div class="product-rule"></div>
        <p class="product-desc">This is a placeholder version of Lorem Ipsum.</p>
        <p class="product-link">Product Detail &amp; Benefits</p>
        <div class="product-buy"><span class="price">$ 24.99</span><span class="buy-button">BUY NOW</span></div>
      </article>
      <article class="product-card">
        <div class="product-photo" role="img" aria-label="Product box of natural sleep aid with capsules"></div>
        <h3 class="product-name">Natural Sleep<span>Aid</span></h3>
        <div class="product-rule"></div>
        <p class="product-desc">This is a placeholder version of Lorem Ipsum.</p>
        <p class="product-link">Product Detail &amp; Benefits</p>
        <div class="product-buy"><span class="price">$ 24.99</span><span class="buy-button">BUY NOW</span></div>
      </article>
      <article class="product-card">
        <div class="product-photo" role="img" aria-label="Product box of memory supplement with capsules"></div>
        <h3 class="product-name">Memory<span>Supplements</span></h3>
        <div class="product-rule"></div>
        <p class="product-desc">This is a placeholder version of Lorem Ipsum.</p>
        <p class="product-link">Product Detail &amp; Benefits</p>
        <div class="product-buy"><span class="price">$ 24.99</span><span class="buy-button">BUY NOW</span></div>
      </article>
      <article class="product-card">
        <div class="product-photo" role="img" aria-label="Product box of stress supplement with capsules"></div>
        <h3 class="product-name">Stress<span>Supplements</span></h3>
        <div class="product-rule"></div>
        <p class="product-desc">This is a placeholder version of Lorem Ipsum.</p>
        <p class="product-link">Product Detail &amp; Benefits</p>
        <div class="product-buy"><span class="price">$ 24.99</span><span class="buy-button">BUY NOW</span></div>
      </article>
    </div>
  </section>

  <p class="tagline">All of our Herbal Natural Supplements and Skincare Products are made using authentic ancient time tested formulations and have an excellent track record.</p>

  <section class="standards">
    <div class="decor decor-left" role="img" aria-label="Faint figure in a yoga pose"></div>
    <div class="decor decor-right" role="img" aria-label="Faint figure in a yoga pose"></div>

    <div class="video">
      <div class="video-photo" role="img" aria-label="Ginkgo leaves in a mortar on a wooden table"></div>
      <svg class="video-play" width="32" height="32" viewBox="0 0 32 32" aria-hidden="true">
        <circle cx="16" cy="16" r="14.5" fill="rgba(255,255,255,0.25)" stroke="#fff" stroke-width="2"/>
        <path d="M12.5 9.5 L23 16 L12.5 22.5 Z" fill="#fff"/>
      </svg>
      <div class="video-caption">Verdant Harbor &nbsp;:&nbsp; Explore Us</div>
    </div>

    <div class="standards-text">
      <h3 class="standards-title">Our Herbal Supplements and Gold Standards</h3>
      <ul class="standards-list">
        <li><svg width="10" height="11" viewBox="0 0 10 11" aria-hidden="true"><path d="M5 0 C8 3 9 6 5 9 C1 6 2 3 5 0 Z M5 9 V11" fill="var(--green-bright)" stroke="var(--green-bright)"/></svg>All of our products are based on ancient time tested herbal formulas.</li>
        <li><svg width="10" height="11" viewBox="0 0 10 11" aria-hidden="true"><path d="M5 0 C8 3 9 6 5 9 C1 6 2 3 5 0 Z M5 9 V11" fill="var(--green-bright)" stroke="var(--green-bright)"/></svg>All the products are designed to be condition specific.</li>
        <li><svg width="10" height="11" viewBox="0 0 10 11" aria-hidden="true"><path d="M5 0 C8 3 9 6 5 9 C1 6 2 3 5 0 Z M5 9 V11" fill="var(--green-bright)" stroke="var(--green-bright)"/></svg>Non-GMO - All our supplements are made from ingredients that were not genetically engineered.</li>
        <li><svg width="10" height="11" viewBox="0 0 10 11" aria-hidden="true"><path d="M5 0 C8 3 9 6 5 9 C1 6 2 3 5 0 Z M5 9 V11" fill="var(--green-bright)" stroke="var(--green-bright)"/></svg>We have conducted trials and studies on our products.</li>
        <li><svg width="10" height="11" viewBox="0 0 10 11" aria-hidden="true"><path d="M5 0 C8 3 9 6 5 9 C1 6 2 3 5 0 Z M5 9 V11" fill="var(--green-bright)" stroke="var(--green-bright)"/></svg>We have attractive, eco friendly, hygienically packaged products.</li>
        <li><svg width="10" height="11" viewBox="0 0 10 11" aria-hidden="true"><path d="M5 0 C8 3 9 6 5 9 C1 6 2 3 5 0 Z M5 9 V11" fill="var(--green-bright)" stroke="var(--green-bright)"/></svg>All of our products have standardized herbal formulas.</li>
      </ul>
    </div>
  </section>
</body>
</html>
```